Candle company needs a label for candle

Looking for a designer to create my candle label. I am going to attach a few pictures of my vision for the label as well as my Company Logo and jar I have puchased. I'm going for the modern rustic feel but you are the designer and have full trust in your abilities. The label is going to be printed on Kraft paper (2x3) so looking for the font to be black. The candle label MUST include the following information:
Candle Birchway Co.
NO. 01: Eucalyptus + Spearmint
Handmade In NJ
Soy Wax
9oz

Industry/Entity Type

Candle Industry

Colors

Designer to choose colors to be used in the design.

Requirements
Should not have
• Any images

```html
<!DOCTYPE html>
<html lang="en">
<head>
<meta charset="utf-8">
<title>Candle Birchway Co. — Eucalyptus &amp; Spearmint Label</title>
<link rel="stylesheet" href="https://fonts.googleapis.com/css2?family=Josefin+Sans:wght@700&family=Marcellus&display=swap">
<style>
  :root {
    --page: #ffffff;
    --kraft: #c8a981;
    --kraft-light: #d2b58f;
    --ink: #1c1a17;
  }
  html, body {
    margin: 0;
    padding: 0;
    width: 1200px;
    height: 1200px;
    overflow: hidden;
    background: var(--page);
  }
  .canvas {
    position: relative;
    width: 1200px;
    height: 1200px;
    display: flex;
    align-items: center;
    justify-content: center;
  }
  .label {
    position: relative;
    width: 900px;
    height: 600px;
    background: radial-gradient(ellipse at 40% 35%, var(--kraft-light), var(--kraft) 75%);
    color: var(--ink);
    box-sizing: border-box;
  }
  .brand-name {
    position: absolute;
    top: 165px;
    left: 0;
    right: 0;
    margin: 0;
    text-align: center;
    font-family: "Marcellus", serif;
    font-weight: 400;
    font-size: 56px;
    line-height: 1.2;
    letter-spacing: 0.02em;
  }
  .scent {
    position: absolute;
    top: 375px;
    left: 0;
    right: 0;
    text-align: center;
    font-family: "Josefin Sans", sans-serif;
    font-weight: 700;
    font-size: 41px;
    letter-spacing: 0.08em;
    margin: 0;
  }
  .details {
    position: absolute;
    top: 430px;
    left: 126px;
    right: 126px;
    height: 58px;
    border-top: 2px dotted var(--ink);
    border-bottom: 2px dotted var(--ink);
    display: grid;
    grid-template-columns: 1fr 1fr 1fr;
    align-items: center;
    font-family: "Marcellus", serif;
  }
  .details span {
    text-align: center;
    font-size: 32px;
    border-left: 2px dotted var(--ink);
    height: 36px;
    line-height: 38px;
  }
  .details span:first-child { border-left: none; }
  .details .wax {
    font-size: 27px;
    letter-spacing: 0.08em;
  }
  .origin {
    position: absolute;
    top: 504px;
    left: 0;
    right: 0;
    text-align: center;
    font-family: "Marcellus", serif;
    font-size: 23px;
    letter-spacing: 0.04em;
    margin: 0;
  }
</style>
</head>
<body>
  <main class="canvas">
    <section class="label" aria-label="Candle jar label">
      <p class="brand-name">Candle Birchway Co.</p>
      <h1 class="scent">EUCALYPTUS &amp; SPEARMINT</h1>
      <div class="details">
        <span class="number">No.01</span>
        <span class="wax">SOY WAX</span>
        <span class="weight">9oz</span>
      </div>
      <p class="origin">HANDMADE IN NJ</p>
    </section>
  </main>
</body>
</html>
```